Corvane Supplies Business Card

Professional business card that stand out to our potential customers. Front and back with clean modern design

Industry/Entity Type

Oil and gas

Contact Information for Business Card

Name, address, website , office phone and cell number

Requirements
Must have
• Editable files for each employee

```html
<!DOCTYPE html>
<html lang="en">
<head>
<meta charset="utf-8">
<title>Corvane Supplies Business Card</title>
<link rel="stylesheet" href="https://fonts.googleapis.com/css2?family=Lexend:wght@400;500;700;800&display=swap">
<style>
  :root{
    --page:#ffffff;
    --card-dark:#121416;
    --card-mid:#2a2e31;
    --card-warm:#3a3430;
    --brand-red:#ff0000;
    --brand-blue:#00b0d0;
    --ink-light:#ffffff;
    --ink-dark:#15181b;
  }
  *{margin:0;padding:0;box-sizing:border-box}
  html,body{width:1200px;height:1200px;overflow:hidden;background:var(--page)}
  body{position:relative;font-family:"Lexend",sans-serif}

  .card{position:absolute;left:208px;width:752px;height:440px;border-radius:20px;overflow:hidden;background:var(--card-dark)}
  .card--front{top:150px}
  .card--back{top:617px}

  .card__photo{position:absolute;inset:0;
    background:
      radial-gradient(ellipse 60% 55% at 62% 45%, rgba(70,74,78,.55), transparent 70%),
      linear-gradient(180deg,var(--card-mid) 0%,var(--card-dark) 55%,var(--card-warm) 78%,var(--card-dark) 100%);}
  .card--front .card__photo::after{content:"";position:absolute;inset:0;
    background:linear-gradient(90deg,transparent 45%,rgba(0,0,0,.85) 75%)}

  .holder__name{position:absolute;left:39px;top:68px;font-size:51px;font-weight:500;color:var(--brand-blue);letter-spacing:-.5px;line-height:1}
  .holder__title{position:absolute;left:44px;top:127px;font-size:26px;font-weight:400;color:var(--brand-blue);line-height:1}

  .contact{position:absolute;left:29px;display:flex;align-items:center;color:var(--brand-red)}
  .contact svg{flex:none}
  .contact--phone{top:244px}
  .contact--phone .contact__text{font-size:38px;font-weight:700;margin-left:10px}
  .contact--email{top:287px}
  .contact--web{top:315px}
  .contact--email .contact__text,.contact--web .contact__text{font-size:19px;margin-left:12px}

  .brand-mark{position:absolute;left:464px;top:150px;width:256px;display:flex;flex-direction:column;align-items:center;gap:14px}
  .brand-mark__square{width:70px;height:70px;background:var(--brand-red)}
  .brand-mark__name{font-size:34px;font-weight:800;color:var(--brand-red);text-align:center;line-height:1.05;text-transform:uppercase}

  .brand-band{position:absolute;left:0;top:394px;width:451px;height:46px;background:var(--brand-red);
    clip-path:polygon(0 0,100% 0,96% 100%,0 100%);display:flex;align-items:center;padding-left:10px}
  .brand-band__name{font-size:27px;font-weight:800;color:var(--ink-dark);text-transform:uppercase;letter-spacing:.5px}

  .social{position:absolute;left:470px;top:402px;display:flex;align-items:center;gap:10px;color:var(--brand-red)}
  .social__label{font-size:19px;font-weight:500;text-transform:uppercase;margin-right:8px}
  .social__item{font-size:14px;font-weight:500}

  .back-mark{position:absolute;left:70px;top:204px;width:602px;height:66px;background:var(--brand-red);
    display:flex;align-items:center;justify-content:center;gap:18px}
  .back-mark__square{width:30px;height:30px;background:var(--ink-light)}
  .back-mark__name{font-size:42px;font-weight:800;color:var(--ink-light);text-transform:uppercase;letter-spacing:1px}
</style>
</head>
<body>

<section class="card card--front">
  <div class="card__photo" role="img" aria-label="Dusky photograph of an offshore oil platform at sea"></div>

  <h1 class="holder__name">Dorian Kell</h1>
  <p class="holder__title">Managing Director</p>

  <p class="contact contact--phone">
    <svg width="34" height="34" viewBox="0 0 24 24" aria-hidden="true"><path fill="#00b0d0" d="M6.6 10.8a15.1 15.1 0 0 0 6.6 6.6l2.2-2.2a1 1 0 0 1 1-.25 11.4 11.4 0 0 0 3.6.57 1 1 0 0 1 1 1V20a1 1 0 0 1-1 1A17 17 0 0 1 3 4a1 1 0 0 1 1-1h3.5a1 1 0 0 1 1 1c0 1.25.2 2.45.57 3.57a1 1 0 0 1-.25 1z"/></svg>
    <span class="contact__text">555 014 2238</span>
  </p>
  <p class="contact contact--email">
    <svg width="28" height="20" viewBox="0 0 28 20" aria-hidden="true"><rect x="1" y="1" width="26" height="18" fill="#00b0d0"/><path d="M1 1l13 10L27 1M1 19l9-9M27 19l-9-9" stroke="#121416" stroke-width="2" fill="none"/></svg>
    <span class="contact__text">dorian.kell@mailbox.com</span>
  </p>
  <p class="contact contact--web">
    <svg width="28" height="28" viewBox="0 0 24 24" aria-hidden="true"><g fill="none" stroke="#00b0d0" stroke-width="2"><circle cx="12" cy="12" r="9"/><path d="M3 12h18M12 3c3 3 3 15 0 18M12 3c-3 3-3 15 0 18"/></g></svg>
    <span class="contact__text">corvanesupplies.com</span>
  </p>

  <div class="brand-mark">
    <span class="brand-mark__square"></span>
    <span class="brand-mark__name">Corvane Supplies</span>
  </div>

  <div class="brand-band"><span class="brand-band__name">Corvane Supplies</span></div>

  <div class="social">
    <span class="social__label">Find us on:</span>
    <span class="social__item">Nexa</span>
    <span class="social__item">Lumo</span>
    <span class="social__item">Chirro</span>
  </div>
</section>

<section class="card card--back">
  <div class="card__photo" role="img" aria-label="Dusky photograph of an offshore oil platform over calm water"></div>
  <div class="back-mark">
    <span class="back-mark__square"></span>
    <span class="back-mark__name">Corvane Supplies</span>
  </div>
</section>

</body>
</html>
```